Restaurant needs a vertical banner for fried catfish

Our restaurant is looking for an eye-catching 78.75in. x 36in. vertical physical banner ad for our fried catfish. Photos for the fried catfish will be provided as a reference but we will also accept anything similar to the photo. We will be using the following as our receptacle: https://www.plankoria.example/banner-stand/retractable-banner-stands/
The design must incorporate the following flavor texts:
Fried Catfish
Always Fresh!
Made from Scratch
Hand-cut Fillets
The Best Catfish in Texas
Served with fries, hush puppies, and a 32oz fountain drink
Also available by the pound!
The final design should be creative, professional, and eye-catching for customers.
Updates
Colors
Designer to choose colors to be used in the design.
Requirements
Must have
- We are open to any and all design elements, albeit the 'flavor texts' should not overpower, but complement the fried catfish photo. 'Fried Catfish' can be used in lieu of a main title/logo.
Nice to have
- Transparent or textured backgrounds that can encompass any or all part of the banner such as a cutting board, shadows, abstract, etc to show depth are a plus.
- Use of vectors or objects such as ribbons or shapes to encapsulate the 'flavor texts' are also encouraged.

```html
<!DOCTYPE html>
<html lang="en">
<head>
<meta charset="utf-8">
<title>Fried Catfish Vertical Banner – Two Colourways</title>
<link rel="stylesheet" href="https://fonts.googleapis.com/css2?family=Crimson+Pro:wght@400;700&family=Fredoka:wght@700&family=Poppins:ital,wght@1,800&display=swap">
<style>
  :root {
    --stage-top: #343434;
    --stage-bottom: #9a9a9a;
    --orange: #c16d00;
    --orange-line: #e8902a;
    --brown: #6b4500;
    --rust: #6b2800;
    --teal: #1789ac;
    --sky: #00b4e6;
    --navy: #003550;
    --shadow-ink: #1d2a4a;
    --bright-blue: #1aa0d8;
    --white: #ffffff;
    --black: #111111;
  }
  html, body {
    margin: 0;
    width: 1200px;
    height: 1200px;
    overflow: hidden;
  }
  body {
    background: linear-gradient(180deg, var(--stage-top), var(--stage-bottom));
    position: relative;
  }
  .banner {
    position: absolute;
    width: 480px;
    height: 1047px;
    display: block;
  }
  .banner--orange { left: 100px; top: 75px; }
  .banner--teal { left: 620px; top: 78px; }
  .headline-fresh {
    font-family: "Poppins", sans-serif;
    font-style: italic;
    font-weight: 800;
    font-size: 62px;
  }
  .headline-title {
    font-family: "Fredoka", sans-serif;
    font-weight: 700;
    font-size: 92px;
  }
  .tagline {
    font-family: "Crimson Pro", serif;
    font-size: 30px;
  }
  .feature-text {
    font-family: "Crimson Pro", serif;
    font-size: 44px;
  }
  .serving-text {
    font-family: "Crimson Pro", serif;
    font-size: 37px;
  }
  .pound-text {
    font-family: "Crimson Pro", serif;
    font-weight: 700;
    font-size: 28px;
  }
</style>
</head>
<body>

<!-- Orange colourway -->
<svg class="banner banner--orange" viewBox="0 0 480 1047" xmlns="http://www.w3.org/2000/svg">
  <defs>
    <linearGradient id="plate-orange" x1="0" y1="0" x2="1" y2="1">
      <stop offset="0" stop-color="#d6a35a"/>
      <stop offset="0.5" stop-color="#b8742e"/>
      <stop offset="1" stop-color="#e9e2d6"/>
    </linearGradient>
  </defs>
  <rect class="banner-bg" width="480" height="1047" fill="var(--orange)"/>

  <!-- faint backdrop behind photo -->
  <rect x="50" y="380" width="380" height="300" rx="40" fill="#e7a550" opacity="0.35" transform="rotate(-12 240 530)" role="img" aria-label="Faded enlarged view of the catfish plate"/>

  <!-- frame outlines -->
  <g class="photo-frames" fill="none" stroke="var(--orange-line)" stroke-width="4">
    <rect x="77" y="331" width="329" height="329" rx="30"/>
    <rect x="77" y="331" width="329" height="329" rx="30" transform="rotate(45 241 496)"/>
  </g>

  <!-- faint lower pattern lines -->
  <g fill="none" stroke="#a85e00" stroke-width="3" opacity="0.6">
    <path d="M60 900 l-40 -40 l80 -80 M480 840 l-120 120 M280 1000 l-60 -60"/>
  </g>

  <!-- headline ribbon -->
  <polygon class="ribbon" points="0,238 480,101 480,256 0,388" fill="var(--brown)"/>
  <g transform="rotate(-16 240 200)">
    <text class="headline-fresh" x="243" y="128" text-anchor="middle" textLength="440" fill="var(--shadow-ink)">Always Fresh!</text>
    <text class="headline-fresh" x="240" y="125" text-anchor="middle" textLength="440" fill="var(--bright-blue)">Always Fresh!</text>
    <text class="headline-title" x="245" y="255" text-anchor="middle" textLength="450" fill="var(--shadow-ink)">Fried Catfish</text>
    <text class="headline-title" x="241" y="251" text-anchor="middle" textLength="450" fill="var(--white)">Fried Catfish</text>
    <text class="tagline" x="262" y="295" text-anchor="middle" textLength="340" fill="var(--white)">The Best Catfish in Texas</text>
  </g>

  <!-- photo -->
  <rect x="108" y="420" width="264" height="150" fill="url(#plate-orange)" stroke="var(--orange-line)" stroke-width="2" role="img" aria-label="Photo of fried catfish fillets with fries, hush puppies, tartar sauce, tomatoes and lemons"/>

  <!-- feature band -->
  <rect y="681" width="480" height="106" fill="var(--brown)"/>
  <text class="feature-text" x="240" y="726" text-anchor="middle" fill="var(--white)">Made from Scratch</text>
  <text class="feature-text" x="240" y="775" text-anchor="middle" fill="var(--white)">Hand-cut Fillets</text>

  <!-- serving details -->
  <text class="serving-text" x="240" y="847" text-anchor="middle" fill="var(--white)">Served with fries,</text>
  <text class="serving-text" x="240" y="895" text-anchor="middle" fill="var(--white)">hush puppies,</text>
  <text class="serving-text" x="240" y="943" text-anchor="middle" fill="var(--white)">and a 32oz fountain drink</text>

  <!-- footer band -->
  <rect y="982" width="480" height="65" fill="var(--rust)"/>
  <text class="pound-text" x="240" y="1024" text-anchor="middle" fill="var(--white)">Also available by the pound!</text>
</svg>

<!-- Teal colourway -->
<svg class="banner banner--teal" viewBox="0 0 480 1047" xmlns="http://www.w3.org/2000/svg">
  <defs>
    <linearGradient id="plate-teal" x1="0" y1="0" x2="1" y2="1">
      <stop offset="0" stop-color="#d6a35a"/>
      <stop offset="0.5" stop-color="#b8742e"/>
      <stop offset="1" stop-color="#e9e2d6"/>
    </linearGradient>
  </defs>
  <rect class="banner-bg" width="480" height="1047" fill="var(--teal)"/>

  <!-- faint backdrop photos -->
  <rect x="30" y="10" width="380" height="230" fill="#4aa6bf" opacity="0.45" transform="rotate(-14 220 125)" role="img" aria-label="Faded view of the catfish plate"/>
  <rect x="10" y="380" width="440" height="300" fill="#4aa6bf" opacity="0.45" transform="rotate(-18 230 530)" role="img" aria-label="Faded view of the catfish plate"/>

  <!-- faint lower pattern lines -->
  <g fill="none" stroke="#20a3cc" stroke-width="3" opacity="0.6">
    <path d="M440 640 l40 40 M420 780 l-80 80 l60 60 M0 900 l40 -40 l-40 -40 M300 1000 l60 -60 l80 80"/>
  </g>

  <!-- headline ribbon -->
  <polygon class="ribbon" points="0,236 480,102 480,258 0,391" fill="var(--sky)"/>
  <g transform="rotate(-16 240 200)">
    <text class="headline-fresh" x="240" y="126" text-anchor="middle" textLength="440" fill="var(--shadow-ink)">Always Fresh!</text>
    <text class="headline-fresh" x="237" y="123" text-anchor="middle" textLength="440" fill="var(--white)">Always Fresh!</text>
    <text class="headline-title" x="245" y="259" text-anchor="middle" textLength="450" fill="var(--shadow-ink)">Fried Catfish</text>
    <text class="headline-title" x="241" y="255" text-anchor="middle" textLength="450" fill="var(--white)">Fried Catfish</text>
    <text class="tagline" x="262" y="302" text-anchor="middle" textLength="340" fill="var(--black)">The Best Catfish in Texas</text>
  </g>

  <!-- photo with white frame -->
  <rect x="43" y="409" width="393" height="226" fill="var(--white)"/>
  <rect x="51" y="416" width="377" height="212" fill="url(#plate-teal)" role="img" aria-label="Photo of fried catfish fillets with fries, hush puppies, tartar sauce, tomatoes and lemons"/>

  <!-- feature band -->
  <rect y="682" width="480" height="108" fill="var(--white)"/>
  <text class="feature-text" x="240" y="728" text-anchor="middle" fill="var(--black)">Made from Scratch</text>
  <text class="feature-text" x="240" y="777" text-anchor="middle" fill="var(--black)">Hand-cut Fillets</text>

  <!-- serving details -->
  <text class="serving-text" x="240" y="851" text-anchor="middle" fill="var(--white)">Served with fries,</text>
  <text class="serving-text" x="240" y="899" text-anchor="middle" fill="var(--white)">hush puppies,</text>
  <text class="serving-text" x="240" y="947" text-anchor="middle" fill="var(--white)">and a 32oz fountain drink</text>

  <!-- footer band -->
  <rect y="986" width="480" height="61" fill="var(--navy)"/>
  <text class="pound-text" x="240" y="1026" text-anchor="middle" fill="var(--white)">Also available by the pound!</text>
</svg>

</body>
</html>
```